Business Card Design

I am selling Cruelty Free/not tested on animal products.
Ideally I would like pictures of rabbits/guinea pigs/Beagle(dog)/rat/mice, as these are the main creatures that are tested on.
Background of card Earth, clouds or rainbow.
Yes I am an animal activist.
My favorite colours are purple and green.

Reason: havent got the perfect design as yet

Industry/Entity Type

Business

Contact Information for Business Card

GENTLY BY NATURE
Cruelty Free Products
Norma Faldt
0492 837 514

```html
<!DOCTYPE html>
<html lang="en">
<head>
<meta charset="utf-8">
<title>Gently By Nature – Business Card</title>
<link rel="stylesheet" href="https://fonts.googleapis.com/css2?family=Cormorant+Garamond:ital,wght@0,500;1,500&display=swap">
<style>
  :root {
    --page-bg: #d9d9d9;
    --ink: #0d0d12;
    --glow: rgba(255, 255, 255, 0.85);
    --scene-top: #a6b4ea;
    --scene-mid: #c3d6f2;
    --scene-low: #9fcf88;
    --guinea-tone: #c49a72;
    --beagle-tone: #b08a6a;
  }
  html, body {
    margin: 0;
    width: 1200px;
    height: 1000px;
    overflow: hidden;
    background: var(--page-bg);
  }
  .canvas {
    position: relative;
    width: 1200px;
    height: 1000px;
  }
  .business-card {
    position: absolute;
    left: 150px;
    top: 210px;
    width: 900px;
    height: 580px;
    border-radius: 16px;
    overflow: hidden;
    box-shadow: 0 10px 28px rgba(0, 0, 0, 0.25);
  }
  .card-scene {
    position: absolute;
    inset: 0;
    background: linear-gradient(180deg, var(--scene-top) 0%, var(--scene-mid) 60%, var(--scene-low) 100%);
  }
  .animal {
    position: absolute;
    border-radius: 24px;
  }
  .animal--guinea-pig {
    left: 40px;
    top: 380px;
    width: 200px;
    height: 180px;
    background: var(--guinea-tone);
  }
  .animal--beagle {
    left: 640px;
    top: 320px;
    width: 230px;
    height: 250px;
    background: var(--beagle-tone);
  }
  .card-text {
    position: absolute;
    left: 0;
    right: 0;
    text-align: center;
    margin: 0;
    color: var(--ink);
    font-family: "Cormorant Garamond", Georgia, serif;
    text-shadow: 0 0 6px var(--glow), 0 0 2px var(--glow);
    line-height: 1;
    padding-right: 12px;
  }
  .brand-name {
    top: 92px;
    font-weight: 500;
    font-size: 70px;
    letter-spacing: 0.5px;
  }
  .brand-tagline {
    top: 166px;
    font-style: italic;
    font-weight: 500;
    font-size: 48px;
  }
  .contact-name {
    top: 306px;
    font-style: italic;
    font-weight: 500;
    font-size: 46px;
  }
  .contact-phone {
    top: 356px;
    font-style: italic;
    font-weight: 500;
    font-size: 34px;
  }
</style>
</head>
<body>
<main class="canvas">
  <section class="business-card">
    <div class="card-scene" role="img" aria-label="Sky with pink clouds above a grassy meadow"></div>
    <div class="animal animal--guinea-pig" role="img" aria-label="Brown and white guinea pig sitting in the grass"></div>
    <div class="animal animal--beagle" role="img" aria-label="Beagle puppy lying in the grass"></div>

    <h1 class="card-text brand-name">GENTLY BY NATURE</h1>
    <p class="card-text brand-tagline">Cruelty Free Products</p>
    <p class="card-text contact-name">Norma Faldt</p>
    <p class="card-text contact-phone">Phone : 0492 837 514</p>
  </section>
</main>
</body>
</html>
```